Zielgruppe
Wir verkaufen spezielle Teemischungen an Frauen, die schwanger werden möchten und sich gezielt ein Mädchen oder einen Jungen wünschen. Die Rezeptur unseres Tees, ist speziell auf den jeweiligen Wunsch abgestimmt. Wir verkaufen daher einen Sonnenwiese Tee und einen Bergquelle Tee.
Aufgabenstellung
Wir benötigen ein Etikett Design für den Sonnenwiese Tee. Wenn das Etikett fertig designed wurde, würden wir gerne anschließend ein Etikett für den Bergquelle Tee designen lassen. Das Design sollte klar, hochwertig und modern wirken. Es sollte erkennbar sein, dass der Tee speziell für Frauen mit einem Mädchenwunsch ist. Die Hintergrundfarbe des Designes bzw. des Etiketts sollte in zart rosa sein.

```html
<!DOCTYPE html>
<html lang="de">
<head>
<meta charset="utf-8">
<title>Sonnenwiese Tee – Etikett</title>
<link href="https://fonts.googleapis.com/css2?family=Roboto:wght@300;400;500;700&display=swap" rel="stylesheet">
<style>
  :root {
    --stage: #e4e4e4;
    --white: #ffffff;
    --magenta: #c8468f;
    --magenta-deep: #bf3c86;
    --rose-title: #e77fa4;
    --rose-soft: #f5c9dd;
    --rose-text: #cf4580;
    --sky: #80c5d5;
    --ink-blue: #2f4f62;
    --badge-text: #f3f8fa;
  }
  * { margin: 0; padding: 0; box-sizing: border-box; }
  html, body { width: 1200px; height: 965px; overflow: hidden; }
  body {
    background: var(--stage);
    font-family: "Roboto", sans-serif;
    position: relative;
  }
  .label {
    position: absolute;
    left: 335px; top: 32px;
    width: 530px; height: 900px;
    border-radius: 22px;
    overflow: hidden;
    background: var(--white);
    box-shadow: 0 6px 24px rgba(0,0,0,0.12);
  }
  .label-shapes { position: absolute; inset: 0; }
  .brand {
    position: absolute; top: 150px; left: 0; width: 100%;
    display: flex; align-items: center; justify-content: center; gap: 14px;
  }
  .brand-dot {
    width: 34px; height: 34px; border-radius: 50%;
    background: var(--rose-title);
  }
  .brand-name {
    font-weight: 300; font-size: 54px; letter-spacing: 2px;
    color: var(--rose-title);
  }
  .product-title {
    position: absolute; top: 286px; left: 0; width: 100%;
    text-align: center;
    font-weight: 700; font-size: 37px; letter-spacing: 0.5px;
    color: var(--rose-title);
  }
  .benefits {
    position: absolute; top: 408px; left: 46px;
    list-style: none;
  }
  .benefits li {
    display: flex; align-items: center; gap: 10px;
    height: 32px;
    color: var(--white); font-weight: 500; font-size: 16px;
  }
  .benefits li::before {
    content: ""; width: 20px; height: 20px; border-radius: 50%;
    background: var(--rose-soft); opacity: 0.8; flex: none;
  }
  .prep {
    position: absolute; top: 652px; left: 40px; right: 30px;
    font-size: 10.5px; line-height: 1.55; color: var(--ink-blue);
  }
  .prep strong { font-weight: 500; font-size: 12px; }
  .info-box {
    position: absolute; top: 768px; left: 60px;
    width: 335px; height: 112px;
    background: var(--rose-soft); border-radius: 8px;
    padding: 12px 18px;
    font-size: 10px; color: var(--rose-text); line-height: 1.45;
  }
  .info-cols { display: flex; gap: 30px; }
  .info-box strong { font-weight: 700; }
  .info-note { margin-top: 8px; }
  .info-company { margin-top: 6px; }
  .weight-badge {
    position: absolute; top: 808px; left: 416px;
    width: 76px; height: 76px; border-radius: 50%;
    background: var(--sky);
    display: flex; flex-direction: column; align-items: center; justify-content: center;
    color: var(--badge-text);
  }
  .weight-badge small { font-size: 8px; }
  .weight-badge span { font-size: 24px; font-weight: 400; line-height: 1; }
</style>
</head>
<body>
  <div class="label">
    <svg class="label-shapes" viewBox="0 0 530 900" width="530" height="900" aria-hidden="true">
      <polygon points="0,362 530,414 530,900 0,900" fill="var(--magenta)"/>
      <polygon points="0,645 530,638 530,738 0,748" fill="var(--sky)"/>
      <rect x="0" y="748" width="530" height="152" fill="var(--magenta-deep)"/>
    </svg>

    <div class="brand">
      <div class="brand-dot"></div>
      <div class="brand-name">Lunavia</div>
    </div>

    <h1 class="product-title">SONNENWIESE TEE</h1>

    <ul class="benefits">
      <li>100% natürlich</li>
      <li>aus kontrolliertem Anbau</li>
      <li>Premium Qualität</li>
      <li>Vegan</li>
      <li>Glutenfrei</li>
      <li>enthält Matcha</li>
      <li>spezielle Rezeptur bei bestehendem Mädchenwunsch</li>
    </ul>

    <div class="prep">
      <p><strong>Zubereitung:</strong> 1-2 Teelöffel pro Tasse (200 ml) bei 100°C 4-6 Minuten lang ziehen lassen.</p>
      <p><strong>Zutaten:</strong> Frauenmantelkraut*, Brennnesselblätter*, Schafgarbe*, Rosmarin*, Apfelstücke*, Hibiskusblüten*, Basilikum*, Holunderblüten*, Eisenkraut*, Matcha.<br>*aus kontrolliertem Anbau</p>
    </div>

    <div class="info-box">
      <div class="info-cols">
        <div><strong>Fragen?</strong><br>info@lunavia.de www.lunavia.de</div>
        <div><strong>Folge uns!</strong><br>FB Lunavia Insta Lunavia</div>
      </div>
      <p class="info-note">Kühl und trocken lagern. Mindestens haltbar bis: Siehe Etikett</p>
      <p class="info-company"><strong>Lunavia GmbH</strong><br>Am Lindenhang 24<br>D-50321 Feldbrück</p>
    </div>

    <div class="weight-badge">
      <small>Nettogewicht</small>
      <span>75g</span>
    </div>
  </div>
</body>
</html>
```